CoveysArmsPersonal

I am a cutting edge, top of the line gun store. We are expanding faster than we can keep up. We offer: Gunsmithing, Transfers, Concealed Carry, Machine Guns, Suppressors. My colors are reflected in my logo. Red, black and white. I like a clean design that gets the point across. I was trying to find a plastic business card, but will settle with a high quality paper product.

Contact Information for Business Card

Dwayne Covey - Owner
620-514-8826 (Cell)
Covey's Range Outfitters
1847 E. Hwy 9
Ravenfield, OK 67462
sales@coveysrangeoutfitters.com
coveysrangeoutfitters.com

```html
<!DOCTYPE html>
<html lang="en">
<head>
<meta charset="utf-8">
<title>Covey's Range Outfitters – Business Card</title>
<link href="https://fonts.googleapis.com/css2?family=Jost:wght@300;400;600;700&display=swap" rel="stylesheet">
<style>
  :root {
    --stage: #2f2f2f;
    --paper: #ffffff;
    --ink: #1c1c1c;
    --muted: #6b6b6b;
    --brand-red: #8b0a14;
    --brand-rose: #c98a90;
  }
  * { box-sizing: border-box; margin: 0; padding: 0; }
  html, body {
    width: 1135px; height: 1200px; overflow: hidden;
    background: var(--stage);
    font-family: "Jost", sans-serif;
  }
  .business-card {
    position: absolute; left: 147px; top: 60px;
    width: 840px; height: 480px;
    background: var(--paper);
    overflow: hidden;
  }
  .card-band { position: absolute; inset: 0; }
  .holder-name {
    position: absolute; left: 70px; top: 78px;
    font-weight: 700; font-size: 44px; letter-spacing: 5px;
    color: var(--brand-red); text-transform: uppercase; line-height: 1;
  }
  .holder-title {
    position: absolute; left: 70px; top: 124px;
    font-weight: 300; font-size: 28px; letter-spacing: 3px;
    color: var(--muted); line-height: 1;
  }
  .contact-list {
    position: absolute; left: 70px; top: 172px;
    list-style: none; color: var(--ink);
    font-size: 19px; letter-spacing: 1.5px; line-height: 1.15;
  }
  .contact-item { display: flex; align-items: flex-start; gap: 12px; margin-bottom: 14px; }
  .contact-icon { flex: none; width: 22px; height: 22px; margin-top: 1px; }
  .contact-phone { font-size: 22px; letter-spacing: 3px; }
  .company-mark {
    position: absolute; right: 56px; top: 96px;
    display: flex; align-items: center; gap: 12px;
  }
  .company-mark-dot { width: 22px; height: 22px; border-radius: 50%; background: var(--brand-red); }
  .company-mark-name {
    font-weight: 600; font-size: 20px; letter-spacing: 2px;
    color: var(--ink); text-transform: uppercase; line-height: 1.1;
  }
  .brand-panel {
    position: absolute; left: 0; top: 600px;
    width: 1135px; height: 540px;
    background: var(--paper);
    display: flex; flex-direction: column; align-items: center; justify-content: center; gap: 26px;
  }
  .brand-panel-dot { width: 120px; height: 120px; border-radius: 50%; background: var(--ink); }
  .brand-panel-name {
    font-weight: 600; font-size: 54px; letter-spacing: 6px;
    color: var(--ink); text-transform: uppercase; text-align: center; line-height: 1.15;
  }
</style>
</head>
<body>
  <article class="business-card">
    <svg class="card-band" viewBox="0 0 840 480" width="840" height="480" aria-hidden="true">
      <path d="M0 350 Q420 336 840 262 L840 480 L0 480 Z" fill="var(--brand-rose)"/>
      <path d="M0 362 Q420 348 840 274 L840 480 L0 480 Z" fill="var(--paper)"/>
      <path d="M0 374 Q420 360 840 286 L840 480 L0 480 Z" fill="var(--brand-red)"/>
      <text x="120" y="448" transform="rotate(-5 120 448)" fill="#fff"
            font-family="Jost, sans-serif" font-size="26" letter-spacing="4">coveysrangeoutfitters.com</text>
    </svg>

    <h1 class="holder-name">Dwayne Covey</h1>
    <p class="holder-title">OWNER</p>

    <ul class="contact-list">
      <li class="contact-item">
        <svg class="contact-icon" viewBox="0 0 24 24" aria-hidden="true">
          <path d="M12 2C8 2 5 5 5 9c0 5 7 13 7 13s7-8 7-13c0-4-3-7-7-7z" fill="none" stroke="var(--brand-red)" stroke-width="2.4"/>
          <circle cx="12" cy="9" r="2.5" fill="var(--brand-red)"/>
        </svg>
        <span>Covey's Range Outfitters<br>1847 E. Hwy 9 Ravenfield, OK<br>67462</span>
      </li>
      <li class="contact-item">
        <svg class="contact-icon" viewBox="0 0 24 24" aria-hidden="true">
          <rect width="24" height="24" rx="5" fill="var(--brand-red)"/>
          <path d="M7 5l3 3-2 2c1 2 3 4 5 5l2-2 3 3-2 3C10 18 6 14 5 8z" fill="#fff"/>
        </svg>
        <span class="contact-phone">620-514-8826</span>
      </li>
      <li class="contact-item">
        <svg class="contact-icon" viewBox="0 0 24 24" aria-hidden="true">
          <circle cx="12" cy="12" r="12" fill="var(--brand-red)"/>
          <rect x="6" y="8" width="12" height="9" fill="none" stroke="#fff" stroke-width="1.6"/>
          <path d="M6 8l6 5 6-5" fill="none" stroke="#fff" stroke-width="1.6"/>
        </svg>
        <span>sales@coveysrangeoutfitters.com</span>
      </li>
    </ul>

    <div class="company-mark">
      <span class="company-mark-dot"></span>
      <span class="company-mark-name">Covey's<br>Range Outfitters</span>
    </div>
  </article>

  <section class="brand-panel">
    <span class="brand-panel-dot"></span>
    <p class="brand-panel-name">Covey's Range Outfitters</p>
  </section>
</body>
</html>
```